Email Signature Block Design for Law Firm

I would like you to create a similar signature block for my law firm . I saw the email signature block attached as image002.png and wanted a similar design for my law firm. I want to be able to swap the portraits for each of my staff from the final design. Our law firm colors are black, gold, white, red.

Industry/Entity Type

Law

Requirements
Nice to have
• i like the red circle in around the photo in the 8 copper bench design. The 9 Copper Bench desgn is what inspired me to have a signature block design for my firm.

```html
<!DOCTYPE html>
<html lang="en">
<head>
<meta charset="utf-8">
<title>Copper Bench Email Signature</title>
<link rel="stylesheet" href="https://fonts.googleapis.com/css2?family=Bebas+Neue&family=Montserrat:wght@500;600&display=swap">
<style>
  :root{
    --ink:#231f20;
    --text:#1f1f1f;
    --paper-1:#f4f4f4;
    --paper-2:#dcdcdc;
    --red:#d52027;
    --gold:#d9a032;
    --white:#ffffff;
    --portrait-1:#f3e6e7;
    --portrait-2:#2a2526;
  }
  *{margin:0;padding:0;box-sizing:border-box}
  html,body{width:1200px;height:401px;overflow:hidden;background:var(--white)}
  .signature{
    position:relative;width:1200px;height:401px;overflow:hidden;
    background:linear-gradient(135deg,var(--paper-1) 0%,var(--paper-2) 45%,var(--paper-1) 70%,var(--paper-2) 100%);
    font-family:"Montserrat",Arial,sans-serif;color:var(--text);
  }
  .base-band{position:absolute;left:0;top:0;width:1200px;height:401px}
  .firm-tab{
    position:absolute;left:0;top:0;width:312px;height:76px;
    background:var(--ink);border-bottom-right-radius:48px;
  }
  .firm-mark{position:absolute;left:36px;top:18px;width:36px;height:36px;background:var(--gold)}
  .firm-name{
    position:absolute;left:84px;top:28px;
    font-family:"Montserrat",Arial,sans-serif;font-weight:600;font-size:13px;
    letter-spacing:.5px;color:var(--gold);white-space:nowrap;
  }
  .person-name{
    position:absolute;left:101px;top:128px;
    font-family:"Bebas Neue",Impact,sans-serif;font-size:52px;line-height:1;
    letter-spacing:.5px;color:var(--ink);
  }
  .name-rule{position:absolute;left:102px;top:179px;width:150px;height:3px;background:var(--red)}
  .person-role{position:absolute;left:102px;top:188px;font-weight:500;font-size:19px;color:var(--ink)}
  .tagline{
    position:absolute;left:102px;top:300px;width:278px;height:82px;
    border:1.5px solid var(--gold);border-radius:28px;
    display:flex;flex-direction:column;align-items:center;padding-top:10px;
    font-family:"Bebas Neue",Impact,sans-serif;font-size:27px;line-height:26px;
    color:var(--white);text-align:center;
  }
  .tagline-rule{width:149px;height:1.5px;background:var(--gold);margin-top:7px}
  .portrait-ring{
    position:absolute;left:424px;top:32px;width:336px;height:336px;border-radius:50%;
    background:var(--red);box-shadow:0 4px 14px rgba(0,0,0,.25);
  }
  .portrait{
    position:absolute;left:22px;top:22px;width:292px;height:292px;border-radius:50%;
    background:radial-gradient(circle at 50% 38%,#8a6a5a 0 18%,var(--portrait-1) 19% 55%,var(--portrait-2) 56%);
  }
  .contacts{position:absolute;left:828px;top:96px;list-style:none}
  .contact{display:flex;align-items:center;height:26px;margin-bottom:9.5px;font-weight:500;font-size:18px;color:var(--ink)}
  .contact-icon{width:27px;height:27px;border-radius:50%;background:var(--red);margin-right:13px;flex:none}
  .contact-icon svg{width:27px;height:27px;display:block}
  .badge{position:absolute;background:var(--white)}
  .badge-round{left:771px;top:296px;width:74px;height:74px;border-radius:50%;border:3px solid var(--ink);outline:2px solid var(--white)}
  .badge-wide{left:873px;top:311px;width:146px;height:48px;background:#5fc1cf;border-radius:3px}
  .badge-list{left:1048px;top:306px;width:88px;height:55px;background:#4aa3d8;border-radius:3px}
</style>
</head>
<body>
<div class="signature">
  <svg class="base-band" viewBox="0 0 1200 401" aria-hidden="true">
    <path d="M0 292 C 260 268 480 258 600 260 C 760 262 980 270 1200 292 L1200 401 L0 401 Z" fill="var(--ink)"/>
  </svg>

  <header class="firm-tab">
    <span class="firm-mark"></span>
    <span class="firm-name">THE COPPER BENCH, PLLC</span>
  </header>

  <h1 class="person-name">MARCUS BENNETT</h1>
  <div class="name-rule"></div>
  <p class="person-role">Attorney at Law</p>

  <div class="tagline">
    <span>TRANSFORMING LIVES,</span>
    <span>UPLIFTING OUR COMMUNITY</span>
    <span class="tagline-rule"></span>
  </div>

  <div class="portrait-ring">
    <div class="portrait" role="img" aria-label="Staff portrait photo: attorney in dark suit and blue striped tie"></div>
  </div>

  <ul class="contacts">
    <li class="contact"><span class="contact-icon"><svg viewBox="0 0 27 27"><path d="M10 7c1 0 1.5 2.5 1.5 3.5S10 12 10 13s2.5 4 3.5 4 1.5-1.5 2.5-1.5 3.5.5 3.5 1.5-1.5 3-3 3C12 20 7 14 7 10c0-1.5 2-3 3-3z" fill="var(--white)"/></svg></span>555-014-2290</li>
    <li class="contact"><span class="contact-icon"><svg viewBox="0 0 27 27"><path d="M10 7c1 0 1.5 2.5 1.5 3.5S10 12 10 13s2.5 4 3.5 4 1.5-1.5 2.5-1.5 3.5.5 3.5 1.5-1.5 3-3 3C12 20 7 14 7 10c0-1.5 2-3 3-3z" fill="var(--white)"/></svg></span>Fax: 555-014-7735</li>
    <li class="contact"><span class="contact-icon"><svg viewBox="0 0 27 27"><rect x="6.5" y="8.5" width="14" height="10" fill="none" stroke="var(--white)" stroke-width="1.6"/><path d="M6.5 8.5l7 5.5 7-5.5M6.5 18.5l5-4.5M20.5 18.5l-5-4.5" fill="none" stroke="var(--white)" stroke-width="1.4"/></svg></span>mbennett@copperbench.com</li>
    <li class="contact"><span class="contact-icon"><svg viewBox="0 0 27 27"><g fill="none" stroke="var(--white)" stroke-width="1.4"><circle cx="13.5" cy="13.5" r="7"/><ellipse cx="13.5" cy="13.5" rx="3" ry="7"/><path d="M6.5 13.5h14M7.5 10h12M7.5 17h12"/></g></svg></span>copperbenchlaw.com</li>
  </ul>

  <span class="badge badge-round" aria-hidden="true"></span>
  <span class="badge badge-wide" aria-hidden="true"></span>
  <span class="badge badge-list" aria-hidden="true"></span>
</div>
</body>
</html>
```